New business card design for Maplewood Ridge Optometry Clinic

We need a new business card design using our existing logo (uploaded). Please do not include eyes, eye exam charts or beaches, water, sand. The logo I uploaded shows our colors of green and blue, but we are open to seeing it in black OR white. We would like to see something modern and fresh. It will need to be 2 sided. On the front we will need to be able to put a doctors name, for example-Dr Clara Venhuisen and Associates. We will need to be able to change the name to other doctors names when we send for printing. The back of the card should list the following: 1748 Tarrow St, Wasaga Beach (P)705-555-0183 (E) info@mroc-example.ca www.mroc-example.ca. "We are welcoming new patients" and a line for the appointment date and time. I have uploaded the back of a card to give an example

```html
<!DOCTYPE html>
<html lang="en">
<head>
<meta charset="utf-8">
<title>Maplewood Ridge Optometry Clinic – Business Card</title>
<link rel="stylesheet" href="https://fonts.googleapis.com/css2?family=Montserrat:wght@500;700;800&family=Open+Sans:wght@400;600&display=swap">
<style>
  :root {
    --clinic-blue: #3a51a0;
    --clinic-green: #1f9a48;
    --ink-grey: #4a4a4a;
    --card-white: #ffffff;
    --stage: #2e2f31;
  }
  * { box-sizing: border-box; margin: 0; padding: 0; }
  html, body { width: 1200px; height: 900px; overflow: hidden; }
  body {
    background: var(--stage);
    display: flex;
    flex-direction: column;
    align-items: center;
    justify-content: center;
    gap: 44px;
    font-family: "Open Sans", Arial, sans-serif;
  }
  .card {
    width: 630px;
    height: 360px;
    background: var(--card-white);
    border-radius: 3px;
    box-shadow: 0 10px 28px rgba(0,0,0,.45);
    display: flex;
    flex-direction: column;
    align-items: center;
    position: relative;
  }
  .clinic-name {
    font-family: "Montserrat", Arial, sans-serif;
    font-weight: 800;
    color: var(--clinic-blue);
    text-align: center;
    line-height: 1.1;
    display: flex;
    align-items: center;
    gap: 12px;
  }
  .clinic-mark {
    border-radius: 50%;
    background: var(--clinic-green);
    flex: none;
  }
  .rule-heading {
    display: flex;
    align-items: center;
    width: 88%;
    gap: 10px;
    font-family: "Montserrat", Arial, sans-serif;
    font-weight: 800;
    color: var(--clinic-blue);
    white-space: nowrap;
  }
  .rule-heading .rule {
    flex: 1;
    height: 1.5px;
  }
  .rule-heading .rule.left { background: linear-gradient(90deg, rgba(58,81,160,0), var(--clinic-blue)); }
  .rule-heading .rule.right { background: linear-gradient(90deg, var(--clinic-blue), rgba(58,81,160,0)); }

  /* back of card */
  .card-back { padding-top: 60px; }
  .card-back .clinic-name { font-size: 24px; }
  .card-back .clinic-mark { width: 22px; height: 22px; }
  .card-back .rule-heading { margin-top: 34px; font-size: 17px; }
  .appointment-label {
    margin-top: 6px;
    font-family: "Montserrat", Arial, sans-serif;
    font-weight: 500;
    font-size: 15px;
    color: var(--clinic-green);
    letter-spacing: .3px;
  }
  .appointment-fields {
    margin-top: 20px;
    width: 86%;
    display: flex;
    gap: 14px;
    font-family: "Montserrat", Arial, sans-serif;
    font-weight: 800;
    font-size: 15px;
    color: var(--clinic-blue);
  }
  .field { flex: 1; display: flex; align-items: flex-end; gap: 4px; }
  .field .dots { flex: 1; border-bottom: 2px dotted var(--ink-grey); margin-bottom: 4px; }
  .contact {
    margin-top: 28px;
    text-align: center;
    font-size: 14.5px;
    line-height: 1.7;
    color: var(--ink-grey);
  }
  .contact .key, .contact .sep { color: var(--clinic-green); }
  .contact .sep { margin: 0 4px; }

  /* front of card */
  .card-front { padding-top: 84px; }
  .card-front .clinic-name { font-size: 34px; max-width: 90%; }
  .card-front .clinic-mark { width: 30px; height: 30px; }
  .card-front .rule-heading { margin-top: 62px; font-size: 22px; }
  .doctor-title {
    margin-top: 4px;
    font-size: 17px;
    color: var(--ink-grey);
  }
</style>
</head>
<body>

  <section class="card card-back" aria-label="Back of business card">
    <div class="clinic-name"><span class="clinic-mark"></span>Maplewood Ridge Optometry Clinic</div>
    <div class="rule-heading"><span class="rule left"></span>We Are Welcoming New Patients<span class="rule right"></span></div>
    <div class="appointment-label">Your Appointment</div>
    <div class="appointment-fields">
      <div class="field">Date<span class="dots"></span></div>
      <div class="field">Time<span class="dots"></span></div>
    </div>
    <div class="contact">
      <div><span class="key">P.</span> 705-555-0183<span class="sep">|</span>1748 Tarrow St, Wasaga Beach</div>
      <div><span class="key">E.</span> info@mroc-example.ca<span class="sep">|</span>www.mroc-example.ca</div>
    </div>
  </section>

  <section class="card card-front" aria-label="Front of business card">
    <div class="clinic-name"><span class="clinic-mark"></span>Maplewood Ridge Optometry Clinic</div>
    <div class="rule-heading"><span class="rule left"></span>Dr. Clara Venhuisen<span class="rule right"></span></div>
    <div class="doctor-title">Optometrist</div>
  </section>

</body>
</html>
```